Poster for List of Company Values

We need a poster to outline our Values which will be displayed in our office as well as posted on our website and other platforms (so need to allow for some flexibly in its application).

File attached outlines what we currently have with design and also our company style guide.

Note that we are looking for a modern, clean look, which still represents our core activities of construction and environmental services.

You can also reference our website here:

https://quorvelgroup.com.au/

Happy to answer any questions you might have.

Thanks for your interest,
Brent

Target Market(s)

Internal and External clients

Industry/Entity Type

Construction, water and recycling

Font styles to use
Sans Serif

Requirements
Must have
• All values on the one page. Graphic to represent each value. Also needs to use company logo
Nice to have
• Preference for poster to be orientated in landscape
Should not have
• Do not follow example provided, this is only to demonstrate what we have to date and also the text required

```html
<!DOCTYPE html>
<html lang="en">
<head>
<meta charset="utf-8">
<title>Core Values Poster</title>
<link href="https://fonts.googleapis.com/css2?family=Open+Sans:wght@400;600;700;800&display=swap" rel="stylesheet">
<style>
  :root {
    --page: #ffffff;
    --navy: #1f2b68;
    --icon: #3b4766;
    --green: #3aa640;
    --green-dark: #2a8a30;
    --blue: #1558c4;
    --blue-dark: #0e3c8e;
    --yellow: #e1b444;
    --yellow-dark: #cb930f;
    --orange: #f18a30;
    --orange-dark: #df5710;
    --red: #d9263f;
    --red-dark: #b0122d;
    --teal: #10b6a6;
    --teal-dark: #0a877b;
  }
  * { margin: 0; padding: 0; box-sizing: border-box; }
  html, body { width: 800px; height: 1200px; overflow: hidden; background: var(--page); }
  body { font-family: "Open Sans", Arial, sans-serif; position: relative; }
  .poster {
    position: absolute;
    left: 40px;
    top: 345px;
    width: 720px;
    height: 509px;
    background: #fff;
    filter: drop-shadow(0 4px 10px rgba(0,0,0,0.18));
  }
  .poster svg { display: block; width: 100%; height: 100%; }
  .brand-name { font-family: "Open Sans", Arial, sans-serif; font-weight: 700; fill: var(--navy); }
  .title { font-family: "Open Sans", Arial, sans-serif; font-weight: 800; fill: var(--navy); }
  .value-heading { font-family: "Open Sans", Arial, sans-serif; font-weight: 700; fill: #fff; font-size: 30px; text-anchor: middle; }
  .value-text { font-family: "Open Sans", Arial, sans-serif; font-weight: 400; fill: #fff; font-size: 18.5px; text-anchor: middle; }
  .web-address { font-family: "Open Sans", Arial, sans-serif; font-weight: 700; fill: #222; font-size: 28px; letter-spacing: 5px; text-anchor: middle; }
  .icon-ring-outer { fill: #fff; stroke: #888; stroke-width: 1; stroke-dasharray: 2 2; }
  .icon-glyph { fill: var(--icon); }
</style>
</head>
<body>
<div class="poster">
<svg viewBox="0 0 1244 880" xmlns="http://www.w3.org/2000/svg">
  <defs>
    <linearGradient id="col-green" x1="0" y1="0" x2="0" y2="1"><stop offset="0" stop-color="var(--green)"/><stop offset="1" stop-color="var(--green-dark)"/></linearGradient>
    <linearGradient id="col-blue" x1="0" y1="0" x2="0" y2="1"><stop offset="0" stop-color="var(--blue)"/><stop offset="1" stop-color="var(--blue-dark)"/></linearGradient>
    <linearGradient id="col-yellow" x1="0" y1="0" x2="0" y2="1"><stop offset="0" stop-color="var(--yellow)"/><stop offset="1" stop-color="var(--yellow-dark)"/></linearGradient>
    <linearGradient id="col-orange" x1="0" y1="0" x2="0" y2="1"><stop offset="0" stop-color="var(--orange)"/><stop offset="1" stop-color="var(--orange-dark)"/></linearGradient>
    <linearGradient id="col-red" x1="0" y1="0" x2="0" y2="1"><stop offset="0" stop-color="var(--red)"/><stop offset="1" stop-color="var(--red-dark)"/></linearGradient>
    <linearGradient id="col-teal" x1="0" y1="0" x2="0" y2="1"><stop offset="0" stop-color="var(--teal)"/><stop offset="1" stop-color="var(--teal-dark)"/></linearGradient>

    <linearGradient id="floor-green" x1="0" y1="0" x2="0" y2="1"><stop offset="0" stop-color="var(--green-dark)"/><stop offset="1" stop-color="var(--green)"/></linearGradient>
    <linearGradient id="floor-blue" x1="0" y1="0" x2="0" y2="1"><stop offset="0" stop-color="var(--blue-dark)"/><stop offset="1" stop-color="var(--blue)"/></linearGradient>
    <linearGradient id="floor-yellow" x1="0" y1="0" x2="0" y2="1"><stop offset="0" stop-color="var(--yellow-dark)"/><stop offset="1" stop-color="var(--yellow)"/></linearGradient>
    <linearGradient id="floor-orange" x1="0" y1="0" x2="0" y2="1"><stop offset="0" stop-color="var(--orange-dark)"/><stop offset="1" stop-color="var(--orange)"/></linearGradient>
    <linearGradient id="floor-red" x1="0" y1="0" x2="0" y2="1"><stop offset="0" stop-color="var(--red-dark)"/><stop offset="1" stop-color="var(--red)"/></linearGradient>
    <linearGradient id="floor-teal" x1="0" y1="0" x2="0" y2="1"><stop offset="0" stop-color="var(--teal-dark)"/><stop offset="1" stop-color="var(--teal)"/></linearGradient>

    <linearGradient id="skyline-haze" x1="0" y1="0" x2="0" y2="1">
      <stop offset="0" stop-color="#eceef0" stop-opacity="0"/>
      <stop offset="0.5" stop-color="#e4e7ea" stop-opacity="0.7"/>
      <stop offset="1" stop-color="#f2f3f4" stop-opacity="0.3"/>
    </linearGradient>
  </defs>

  <!-- background city haze -->
  <g role="img" aria-label="Faint city skyline of office towers behind the values">
    <rect x="40" y="220" width="1170" height="520" fill="url(#skyline-haze)"/>
  </g>

  <!-- brand -->
  <g class="brand">
    <text class="brand-name" x="78" y="158" font-size="38">QUORVEL</text>
    <text class="brand-name" x="78" y="192" font-size="34">Group</text>
  </g>

  <!-- title -->
  <text class="title" x="275" y="167" font-size="150" textLength="878" lengthAdjust="spacingAndGlyphs">CORE VALUES</text>

  <!-- floor -->
  <g class="floor">
    <polygon points="105,695 276,695 183,880 0,880 0,832" fill="url(#floor-green)"/>
    <polygon points="276,695 449,695 438,740 422,880 183,880" fill="url(#floor-blue)"/>
    <polygon points="449,695 621,695 621,880 422,880 438,740" fill="url(#floor-yellow)"/>
    <polygon points="621,695 794,695 824,880 621,880" fill="url(#floor-orange)"/>
    <polygon points="794,695 967,695 1076,880 824,880" fill="url(#floor-red)"/>
    <polygon points="967,695 1139,695 1244,830 1244,880 1076,880" fill="url(#floor-teal)"/>
  </g>

  <!-- value columns -->
  <g class="columns">
    <polygon points="105,367 163,367 193,338 223,367 276,367 276,695 105,695" fill="url(#col-green)"/>
    <polygon points="276,367 335,367 365,338 395,367 449,367 449,695 276,695" fill="url(#col-blue)"/>
    <polygon points="449,367 505,367 535,338 565,367 621,367 621,695 449,695" fill="url(#col-yellow)"/>
    <polygon points="621,367 676,367 706,338 736,367 794,367 794,695 621,695" fill="url(#col-orange)"/>
    <polygon points="794,367 848,367 878,338 908,367 967,367 967,695 794,695" fill="url(#col-red)"/>
    <polygon points="967,367 1023,367 1053,338 1083,367 1139,367 1139,695 967,695" fill="url(#col-teal)"/>
  </g>

  <!-- icons -->
  <g class="icons">
    <!-- loyal: heart in hand -->
    <g transform="translate(193,275)">
      <circle class="icon-ring-outer" r="52"/>
      <circle r="44" fill="#fff" stroke="var(--green)" stroke-width="4"/>
      <path class="icon-glyph" d="M0,-4 C-14,-14 -14,-28 -5,-28 C-2,-28 0,-25 0,-23 C0,-25 2,-28 5,-28 C14,-28 14,-14 0,-4Z"/>
      <rect class="icon-glyph" x="-22" y="2" width="7" height="20" rx="1"/>
      <path class="icon-glyph" d="M-13,4 L0,4 C5,4 6,10 1,10 L-4,10 L8,10 L20,4 C24,2 27,6 24,9 L10,20 L-13,20Z"/>
    </g>
    <!-- initiative: rocket -->
    <g transform="translate(365,275)">
      <circle class="icon-ring-outer" r="52"/>
      <circle r="44" fill="#fff" stroke="var(--blue)" stroke-width="4"/>
      <g transform="rotate(45)">
        <path class="icon-glyph" d="M0,-28 C10,-18 10,0 8,12 L-8,12 C-10,0 -10,-18 0,-28Z"/>
        <circle r="5" cy="-8" fill="#fff"/>
        <path class="icon-glyph" d="M-8,2 L-16,14 L-8,12Z M8,2 L16,14 L8,12Z"/>
        <path class="icon-glyph" d="M-4,15 L0,26 L4,15Z"/>
      </g>
    </g>
    <!-- team: three people -->
    <g transform="translate(535,275)">
      <circle class="icon-ring-outer" r="52"/>
      <circle r="44" fill="#fff" stroke="var(--yellow)" stroke-width="4"/>
      <circle class="icon-glyph" cx="-14" cy="-14" r="6"/>
      <circle class="icon-glyph" cx="0" cy="-16" r="6.5"/>
      <circle class="icon-glyph" cx="14" cy="-14" r="6"/>
      <rect class="icon-glyph" x="-21" y="-6" width="13" height="22" rx="4"/>
      <rect class="icon-glyph" x="-7" y="-8" width="14" height="26" rx="4"/>
      <rect class="icon-glyph" x="8" y="-6" width="13" height="22" rx="4"/>
    </g>
    <!-- respect: heart handshake -->
    <g transform="translate(706,275)">
      <circle class="icon-ring-outer" r="52"/>
      <circle r="44" fill="#fff" stroke="var(--orange)" stroke-width="4"/>
      <path class="icon-glyph" d="M0,22 C-28,4 -28,-22 -12,-22 C-6,-22 -2,-18 0,-14 C2,-18 6,-22 12,-22 C28,-22 28,4 0,22Z"/>
      <path d="M-14,2 L-4,-6 L6,2 M-8,8 L2,0 M-2,13 L6,6" stroke="#fff" stroke-width="3" fill="none" stroke-linecap="round"/>
    </g>
    <!-- open and honest: clapping hands -->
    <g transform="translate(873,275)">
      <circle class="icon-ring-outer" r="52"/>
      <circle r="44" fill="#fff" stroke="var(--red)" stroke-width="4"/>
      <path class="icon-glyph" d="M-18,-10 C-20,-20 -8,-22 -6,-14 L-2,-20 C2,-26 12,-22 8,-14 L14,-16 C20,-18 24,-10 18,-6 L8,8 C2,18 -10,24 -18,12Z"/>
      <path d="M-12,-6 L-2,4 M-4,-12 L6,-2" stroke="#fff" stroke-width="2.5" stroke-linecap="round"/>
    </g>
    <!-- positive: thumbs up with stars -->
    <g transform="translate(1053,275)">
      <circle class="icon-ring-outer" r="52"/>
      <circle r="44" fill="#fff" stroke="var(--teal)" stroke-width="4"/>
      <rect class="icon-glyph" x="-20" y="-2" width="8" height="22" rx="1"/>
      <path class="icon-glyph" d="M-9,-2 L-2,-14 C0,-18 6,-17 5,-11 L4,-4 L16,-4 C21,-4 22,2 19,4 C22,6 21,11 17,12 C19,15 17,20 12,20 L-9,20Z"/>
      <polygon class="icon-glyph" points="-14,-28 -12,-23 -7,-23 -11,-20 -9,-15 -14,-18 -19,-15 -17,-20 -21,-23 -16,-23"/>
      <polygon class="icon-glyph" points="0,-34 2,-29 7,-29 3,-26 5,-21 0,-24 -5,-21 -3,-26 -7,-29 -2,-29"/>
      <polygon class="icon-glyph" points="14,-28 16,-23 21,-23 17,-20 19,-15 14,-18 9,-15 11,-20 7,-23 12,-23"/>
    </g>
  </g>

  <!-- value text -->
  <g class="value-be-loyal">
    <text class="value-heading" x="188" y="437">be</text>
    <text class="value-heading" x="188" y="466">LOYAL</text>
    <text class="value-text" x="191" y="533">We take care</text>
    <text class="value-text" x="191" y="554">of our own</text>
    <text class="value-text" x="191" y="575">and</text>
    <text class="value-text" x="191" y="596">provide</text>
    <text class="value-text" x="191" y="617">opportunities</text>
    <text class="value-text" x="191" y="638">to listen and</text>
    <text class="value-text" x="191" y="659">support each</text>
    <text class="value-text" x="191" y="680">other.</text>
  </g>
  <g class="value-show-initiative">
    <text class="value-heading" x="363" y="437">show</text>
    <text class="value-heading" x="363" y="466">INITIATIVE</text>
    <text class="value-text" x="360" y="533">We celebrate</text>
    <text class="value-text" x="360" y="554">and recognize</text>
    <text class="value-text" x="360" y="575">our own and</text>
    <text class="value-text" x="360" y="596">encourage</text>
    <text class="value-text" x="360" y="617">forward</text>
    <text class="value-text" x="360" y="638">thinking.</text>
  </g>
  <g class="value-think-team">
    <text class="value-heading" x="532" y="437">think</text>
    <text class="value-heading" x="532" y="466">TEAM</text>
    <text class="value-text" x="534" y="533">We</text>
    <text class="value-text" x="534" y="554">communicate</text>
    <text class="value-text" x="534" y="575">effectively and</text>
    <text class="value-text" x="534" y="596">work as a team</text>
    <text class="value-text" x="534" y="617">by helping and</text>
    <text class="value-text" x="534" y="638">supporting</text>
    <text class="value-text" x="534" y="659">each other.</text>
  </g>
  <g class="value-show-respect">
    <text class="value-heading" x="712" y="437">show</text>
    <text class="value-heading" x="712" y="466">RESPECT</text>
    <text class="value-text" x="715" y="533">We value the</text>
    <text class="value-text" x="715" y="554">diversity</text>
    <text class="value-text" x="715" y="575">and opinions</text>
    <text class="value-text" x="715" y="596">of all.</text>
  </g>
  <g class="value-open-honest">
    <text class="value-heading" x="882" y="437">be OPEN</text>
    <text class="value-heading" x="882" y="466">and</text>
    <text class="value-heading" x="882" y="495">HONEST</text>
    <text class="value-text" x="882" y="533">We are clear and</text>
    <text class="value-text" x="882" y="554">open with each</text>
    <text class="value-text" x="882" y="575">other, and</text>
    <text class="value-text" x="882" y="596">provide an</text>
    <text class="value-text" x="882" y="617">approachable</text>
    <text class="value-text" x="882" y="638">and friendly</text>
    <text class="value-text" x="882" y="659">environment.</text>
  </g>
  <g class="value-positive-smile">
    <text class="value-heading" x="1047" y="441">be</text>
    <text class="value-heading" x="1050" y="470">POSITIVE</text>
    <text class="value-heading" x="1050" y="499">and SMILE</text>
    <text class="value-text" x="1050" y="533">We are</text>
    <text class="value-text" x="1050" y="554">solutions</text>
    <text class="value-text" x="1050" y="575">focused and</text>
    <text class="value-text" x="1050" y="596">encourage a</text>
    <text class="value-text" x="1050" y="617">positive attitude</text>
    <text class="value-text" x="1050" y="638">turning a</text>
    <text class="value-text" x="1050" y="659">negative into a</text>
    <text class="value-text" x="1050" y="680">positive.</text>
  </g>

  <!-- web address pill -->
  <g class="web-pill">
    <rect x="340" y="759" width="550" height="46" rx="23" fill="#fff"/>
    <text class="web-address" x="615" y="792">www.quorvelgroup.com.au</text>
  </g>
</svg>
</div>
</body>
</html>
```